Company letter head and business card for new Indian Pharmaceutical Export company.

We need a letterhead and business card design for an Indian Pharmaceutical Export company.

The letter head needs to contain the following information.
Vorin Healthline Pvt. Ltd.
Office No 4827 Plot No 19, Larkspire, KT Lane, 400153, Maharashtra, India.
Email: info@vorin-healthline.com
Phone: +91-8342196507
CIN: U71853MH2025PTC902617
GSTIN: (This number is still pending, we will add later)

The business card needs to contain:
Address:
Vorin Healthline Pvt. Ltd.
Office No 4827 Plot No19, Larkspire, KT Lane, 400153, MH, India.
Email: torvald@vorin-healthline.com
Phone: +49-17634902851
Name on card: Torvald Ramming
Position: Director

The design for the letter head and business card should be simple but trustworthy.
Please use only Green and blue, same as in the attached logo.

```html
<!DOCTYPE html>
<html lang="en">
<head>
<meta charset="utf-8">
<title>Vorin Healthline – Letterhead and Business Cards</title>
<link href="https://fonts.googleapis.com/css2?family=Montserrat:wght@400;500;600;800&family=Arimo:wght@400&display=swap" rel="stylesheet">
<style>
  :root{
    --page-bg:#e2e2e2;
    --paper:#f1f1f1;
    --brand-blue:#1565a8;
    --deep-blue:#125a98;
    --brand-green:#7cb63a;
    --ink:#333333;
    --ink-soft:#4a4a4a;
    --white:#ffffff;
  }
  *{box-sizing:border-box;margin:0;padding:0}
  html,body{width:1200px;height:839px;overflow:hidden;background:var(--page-bg)}
  body{position:relative;font-family:'Montserrat',sans-serif;color:var(--ink)}

  /* Letterhead */
  .letterhead{position:absolute;left:95px;top:62px;width:494px;height:697px;background:var(--paper);box-shadow:0 4px 14px rgba(0,0,0,.12)}
  .lh-brand{position:absolute;left:28px;top:28px;width:74px;text-align:center}
  .lh-brand .mark{width:58px;height:58px;border-radius:50%;background:var(--brand-blue);margin:0 auto 10px}
  .lh-brand .name{font-weight:800;font-size:8.2px;color:var(--brand-blue);white-space:nowrap;margin-left:-4px}
  .lh-address{position:absolute;right:169px;top:52px;text-align:right;font-size:8.6px;line-height:11.5px;color:var(--ink)}
  .lh-address .company{color:var(--brand-blue);font-weight:600;margin-bottom:1px}
  .lh-divider{position:absolute;left:336px;top:51px;width:1px;height:35px;background:var(--brand-green)}
  .contact-list{list-style:none}
  .contact-list li{display:flex;align-items:center;gap:4px;white-space:nowrap}
  .contact-list svg{width:7px;height:7px;flex:none;fill:var(--brand-green)}
  .lh-contacts{position:absolute;left:345px;top:50px;font-size:8.6px;line-height:13.6px}
  .lh-rule{position:absolute;left:103px;right:25px;top:106px;height:1px;background:var(--brand-green)}
  .recipient{position:absolute;left:28px;top:191px;font-family:'Arimo',sans-serif;font-size:9.2px;line-height:14.2px;color:var(--ink)}
  .letter-body{position:absolute;left:28px;top:256px;width:438px;font-family:'Arimo',sans-serif;font-size:9.2px;line-height:14.2px;color:var(--ink-soft);text-align:justify}
  .letter-body p{margin-bottom:12px}
  .letter-body p.lead{margin-bottom:16px}
  .closing{margin-top:-2px}
  .signature-slot{width:90px;height:34px;margin-top:10px;background:linear-gradient(90deg,#d9d9d9,#e8e8e8);border-radius:3px}
  .lh-footer{position:absolute;left:0;right:0;top:664px;text-align:center;font-size:8.4px;color:var(--ink)}
  .lh-footer .sep{color:var(--brand-green);margin:0 5px}

  /* Business card front */
  .card{position:absolute;width:409px;height:233px;box-shadow:0 6px 14px rgba(0,0,0,.18)}
  .card-front{left:693px;top:152px;background:var(--paper)}
  .cf-brand{position:absolute;left:19px;top:33px;font-weight:800;font-size:20.5px;color:var(--deep-blue)}
  .cf-person{position:absolute;left:19px;top:89px}
  .cf-person .person-name{font-weight:800;font-size:15px;color:var(--deep-blue);line-height:17px}
  .cf-person .role{font-size:9.4px;color:var(--ink);line-height:12px}
  .cf-address{position:absolute;left:19px;top:125px;font-size:9.4px;line-height:12.4px;color:var(--ink)}
  .cf-address .company{color:var(--brand-blue);font-weight:600}
  .cf-contacts{position:absolute;left:19px;top:171px;font-size:9.4px;line-height:15.3px;color:var(--ink)}
  .cf-mark{position:absolute;left:214px;top:26px;width:180px;height:180px;border-radius:50%;background:var(--brand-blue)}

  /* Business card back */
  .card-back{left:695px;top:435px;width:411px;height:235px;background:var(--deep-blue)}
  .cb-mark{position:absolute;left:174px;top:56px;width:60px;height:60px;border-radius:50%;background:var(--white)}
  .cb-name{position:absolute;left:0;right:0;top:168px;text-align:center;font-weight:800;font-size:14px;color:var(--white)}
</style>
</head>
<body>

<section class="letterhead" aria-label="Letterhead">
  <div class="lh-brand">
    <div class="mark"></div>
    <div class="name">Vorin Healthline</div>
  </div>

  <div class="lh-address">
    <div class="company">Vorin Healthline Pvt. Ltd.</div>
    <div>Office No 4827 Plot No 19, Larkspire</div>
    <div>KT Lane, 400153, Maharashtra, India</div>
  </div>
  <div class="lh-divider"></div>
  <ul class="contact-list lh-contacts">
    <li><svg viewBox="0 0 10 10"><path d="M2 0.5 3.8 2.7 2.9 3.8C3.5 5 4.9 6.4 6.2 7.1L7.3 6.2 9.5 8 8.4 9.5C4.6 9.3 0.7 5.4 0.5 1.6Z"/></svg>+91-8342196507</li>
    <li><svg viewBox="0 0 10 10"><path d="M0 2h10v6H0z M0 2l5 3.4L10 2" stroke="#fff" stroke-width=".8"/></svg>info@vorin-healthline.com</li>
    <li><svg viewBox="0 0 10 10"><circle cx="5" cy="5" r="4.6"/><path d="M0.5 5h9M5 .4v9.2M5 .4C2.6 3 2.6 7 5 9.6M5 .4C7.4 3 7.4 7 5 9.6" stroke="#fff" stroke-width=".7" fill="none"/></svg>www.vorin-healthline.com</li>
  </ul>
  <div class="lh-rule"></div>

  <div class="recipient">
    <div>Mr/s</div>
    <div>First Name and Last Name</div>
    <div>Company Name</div>
    <div>Address</div>
  </div>

  <div class="letter-body">
    <p class="lead">Lorem Ipsum is simply dummy text of the printing and typesetting industry. Lorem Ipsum has been the industry's standard dummy text ever since the 1500s, when an unknown printer took a galley of type and scrambled it to make a type specimen book. It has survived not only five centuries, but also the leap into electronic typesetting, remaining essentially unchanged. It was popularised in the 1960s with the release of Letraset sheets containing Lorem Ipsum passages.</p>
    <p>he standard chunk of Lorem Ipsum used since the 1500s is reproduced below for those interested. Sections 1.10.32 and 1.10.33 from "de Finibus Bonorum et Malorum" by Cicero are also reproduced in their exact original form, accompanied by English versions from the 1914 translation by H. Rackham. Lorem ipsum dolor sit amet, consectetur adipiscing elit, sed do eiusmod tempor incididunt ut labore et dolore magna aliqua.</p>
    <p>It is a long established fact that a reader will be distracted by the readable content of a page when looking at its layout. The point of using Lorem Ipsum is that it has a more-or-less normal distribution of letters, as opposed to using 'Content here, content here', making it look like readable English. Many desktop publishing packages and web page editors now .</p>
    <p class="closing">Your Sincerely,</p>
    <div class="signature-slot" role="img" aria-label="Handwritten signature"></div>
  </div>

  <div class="lh-footer">CIN: U71853MH2025PTC902617<span class="sep">|</span>GSTIN: Pending</div>
</section>

<section class="card card-front" aria-label="Business card front">
  <div class="cf-brand">Vorin Healthline</div>
  <div class="cf-person">
    <div class="person-name">Torvald Ramming</div>
    <div class="role">Director</div>
  </div>
  <div class="cf-address">
    <div class="company">Vorin Healthline Pvt. Ltd.</div>
    <div>Office No 4827 Plot No19, Larkspire</div>
    <div>KT Lane, 400153, MH, India</div>
  </div>
  <ul class="contact-list cf-contacts">
    <li><svg viewBox="0 0 10 10"><path d="M2 0.5 3.8 2.7 2.9 3.8C3.5 5 4.9 6.4 6.2 7.1L7.3 6.2 9.5 8 8.4 9.5C4.6 9.3 0.7 5.4 0.5 1.6Z"/></svg>+49-17634902851</li>
    <li><svg viewBox="0 0 10 10"><path d="M0 2h10v6H0z M0 2l5 3.4L10 2" stroke="#fff" stroke-width=".8"/></svg>torvald@vorin-healthline.com</li>
    <li><svg viewBox="0 0 10 10"><circle cx="5" cy="5" r="4.6"/><path d="M0.5 5h9M5 .4v9.2M5 .4C2.6 3 2.6 7 5 9.6M5 .4C7.4 3 7.4 7 5 9.6" stroke="#fff" stroke-width=".7" fill="none"/></svg>www.vorin-healthline.com</li>
  </ul>
  <div class="cf-mark"></div>
</section>

<section class="card card-back" aria-label="Business card back">
  <div class="cb-mark"></div>
  <div class="cb-name">Vorin Healthline</div>
</section>

</body>
</html>
```